Business card for Quorbital, LLC

I need a business card template in .ai or similar format for my IT consultancy, Quorbital(.com)

Front side: The usual name/title/number/fax/email/contact info. Definitely san-serif, the logo font is MuseoSans 500 so the company name (Quorbital, LLC.) should definitely be in the same type and the rest of the text should be that or something complimentary. Including logo on the front is optional - I would prefer designs that include both with and without. I am open to creative input on the format.

Back side: Company logo framed somehow. I was thinking red background with the logo in a white circle in the middle, tho' I'm not sure how that would play off the red ball in the elephant's trunk. Open to creative input here too.

Attached are a (very rough) one-sided card mock-up I made, along with the logo and logo font.

```html
<!DOCTYPE html>
<html lang="en">
<head>
<meta charset="utf-8">
<title>Quorbital, LLC — Business Card</title>
<link rel="stylesheet" href="https://fonts.googleapis.com/css2?family=Nunito+Sans:wght@400;600;800&display=swap">
<style>
  :root {
    --stage: #2b2b2b;
    --card-paper: #f1f1f1;
    --brand-red: #e31e24;
    --brand-red-deep: #b5151b;
    --ink-dark: #3a3a3a;
    --ink-mid: #6d6d6d;
    --ink-soft: #8a8a8a;
    --divider: #dcdcdc;
    --white: #ffffff;
  }
  * { box-sizing: border-box; margin: 0; padding: 0; }
  html, body {
    width: 1200px; height: 900px; overflow: hidden;
    background: var(--stage);
    font-family: "Nunito Sans", sans-serif;
  }
  .card-sheet {
    position: absolute; top: 296px; left: 70px;
    display: flex; gap: 60px;
  }
  .card {
    position: relative; width: 500px; height: 308px; overflow: hidden;
    box-shadow: 0 6px 18px rgba(0,0,0,.45);
  }

  /* Front */
  .card-front { background: var(--card-paper); }
  .card-front .bottom-band { position: absolute; left: 0; bottom: 0; width: 100%; height: 44px; }
  .card-front .divider {
    position: absolute; left: 250px; top: 26px; height: 206px;
    border-left: 1px solid var(--divider);
  }
  .brand-lockup {
    position: absolute; left: 0; top: 0; width: 250px; height: 262px;
    display: flex; flex-direction: column; align-items: center; justify-content: center; gap: 14px;
  }
  .brand-dot { width: 62px; height: 62px; border-radius: 50%; background: var(--ink-dark); }
  .brand-name {
    font-weight: 800; font-size: 34px; letter-spacing: .5px;
    color: var(--brand-red); text-transform: uppercase;
  }
  .contact-block { position: absolute; left: 272px; top: 50px; }
  .person-name { color: var(--brand-red); font-weight: 600; font-size: 23px; line-height: 1; }
  .person-role { color: var(--ink-mid); font-size: 15px; margin-top: 5px; }
  .postal { color: var(--ink-soft); font-size: 13px; line-height: 1.55; margin-top: 20px; }
  .contact-lines { list-style: none; margin-top: 20px; }
  .contact-lines li {
    display: flex; align-items: center; gap: 10px;
    color: var(--ink-soft); font-size: 13px; line-height: 1; margin-bottom: 9px;
  }
  .contact-lines svg { width: 13px; height: 13px; flex: none; fill: var(--ink-soft); }

  /* Back */
  .card-back {
    background: radial-gradient(circle at 55% 40%, var(--brand-red) 0%, var(--brand-red-deep) 100%);
  }
  .emblem {
    position: absolute; left: 50%; top: 50%; width: 236px; height: 236px;
    transform: translate(-50%, -50%); border-radius: 50%; background: var(--white);
    display: flex; flex-direction: column; align-items: center; justify-content: center; gap: 12px;
  }
  .emblem::after {
    content: ""; position: absolute; inset: 7px; border-radius: 50%;
    border: 1.5px solid var(--brand-red);
  }
  .emblem .brand-dot { width: 54px; height: 54px; }
  .emblem .brand-name { font-size: 27px; }
</style>
</head>
<body>
  <main class="card-sheet">
    <section class="card card-front" aria-label="Card front">
      <div class="brand-lockup">
        <span class="brand-dot"></span>
        <span class="brand-name">Quorbital</span>
      </div>
      <span class="divider"></span>
      <div class="contact-block">
        <p class="person-name">Your Name</p>
        <p class="person-role">Position</p>
        <p class="postal">PO Box 1234<br>Yourcity, ST, 41101</p>
        <ul class="contact-lines">
          <li><svg viewBox="0 0 16 16"><rect x="4" y="0" width="8" height="16" rx="1.5"/><rect x="5.5" y="2" width="5" height="9" fill="#f1f1f1"/></svg>102 345 4646</li>
          <li><svg viewBox="0 0 16 16"><rect x="0" y="3" width="16" height="11" rx="1"/><path d="M1 4l7 5 7-5" fill="none" stroke="#f1f1f1" stroke-width="1.5"/></svg>yourmail@quorbital.com</li>
          <li><svg viewBox="0 0 16 16"><circle cx="8" cy="8" r="7.5"/><path d="M0.5 8h15M8 0.5c-3 3-3 12 0 15M8 0.5c3 3 3 12 0 15" fill="none" stroke="#f1f1f1" stroke-width="1"/></svg>www.quorbital.com</li>
        </ul>
      </div>
      <svg class="bottom-band" viewBox="0 0 500 44" preserveAspectRatio="none" aria-hidden="true">
        <path d="M0 44 L0 30 Q250 4 500 30 L500 44 Z" fill="var(--brand-red)"/>
        <path d="M0 30 Q250 4 500 30 Q250 14 0 34 Z" fill="var(--brand-red-deep)" opacity=".5"/>
      </svg>
    </section>

    <section class="card card-back" aria-label="Card back">
      <div class="emblem">
        <span class="brand-dot"></span>
        <span class="brand-name">Quorbital</span>
      </div>
    </section>
  </main>
</body>
</html>
```